Washing Up Liquid Label

We are looking for 2 labels to be designed to be part of a range of products.

The brand is Marlow Brite and we are looking for a label design to you on washing up liquid bottle similar to the ones in the file attached.

One label it be original and the liquid will be green so the label colour needs to be green or work with the green. The other label is lemon and is yellow.

Please see attached the Marlow Brite logo and also a couple of the other designs in the range.

```html
<!DOCTYPE html>
<html lang="en">
<head>
<meta charset="utf-8">
<title>Marlow Brite Washing Up Liquid Labels</title>
<link href="https://fonts.googleapis.com/css2?family=Arimo:wght@700&display=swap" rel="stylesheet">
<style>
  :root {
    --page-bg: #ffffff;
    --brand-blue: #1b3f9e;
    --label-text: #ffffff;
    --green-light: #9ad04a;
    --green-mid: #5fa82e;
    --green-dark: #2c7219;
    --yellow-light: #fff8a8;
    --yellow-mid: #fbe83a;
    --yellow-dark: #ecc900;
    --bubble-light: #eafcff;
    --bubble-mid: #a6def0;
    --bubble-edge: #62b7d6;
    --lemon-light: #fffbd0;
    --lemon-mid: #f5df4c;
  }
  html, body {
    margin: 0;
    padding: 0;
    width: 1022px;
    height: 1200px;
    overflow: hidden;
    background: var(--page-bg);
  }
  .canvas {
    position: relative;
    width: 1022px;
    height: 1200px;
    font-family: "Arimo", Arial, sans-serif;
  }
  .label {
    position: absolute;
    border-radius: 50%;
    box-sizing: border-box;
    box-shadow: 0 6px 18px rgba(0, 0, 0, 0.12);
  }
  .label--original {
    left: 50px;
    top: 250px;
    width: 440px;
    height: 440px;
    background: radial-gradient(circle at 50% 45%, var(--green-light) 0%, var(--green-mid) 62%, var(--green-dark) 100%);
  }
  .label--lemon {
    left: 525px;
    top: 430px;
    width: 470px;
    height: 470px;
    background: radial-gradient(circle at 50% 45%, var(--yellow-light) 0%, var(--yellow-mid) 62%, var(--yellow-dark) 100%);
  }
  .brand {
    position: absolute;
    left: 0;
    right: 0;
    display: flex;
    align-items: center;
    justify-content: center;
    gap: 10px;
    color: var(--brand-blue);
    font-weight: 700;
    line-height: 1;
    white-space: nowrap;
  }
  .brand-dot {
    border-radius: 50%;
    background: var(--brand-blue);
    flex: none;
  }
  .label--original .brand { top: 92px; font-size: 48px; }
  .label--original .brand-dot { width: 18px; height: 18px; }
  .label--lemon .brand { top: 100px; font-size: 52px; }
  .label--lemon .brand-dot { width: 20px; height: 20px; }
  .artwork {
    position: absolute;
  }
  .label--original .artwork {
    left: 80px;
    top: 168px;
    width: 290px;
    height: 180px;
    border-radius: 90px;
    background: radial-gradient(ellipse at 35% 40%, var(--bubble-light) 0%, var(--bubble-mid) 55%, rgba(98, 183, 214, 0.55) 100%);
  }
  .label--lemon .artwork {
    left: 60px;
    top: 178px;
    width: 350px;
    height: 190px;
    border-radius: 95px;
    background: linear-gradient(90deg, var(--lemon-light) 0%, var(--lemon-mid) 38%, var(--bubble-light) 68%, var(--bubble-mid) 100%);
  }
  .variant-name {
    position: absolute;
    color: var(--label-text);
    font-weight: 700;
    font-size: 20px;
    letter-spacing: 0.5px;
    line-height: 1;
  }
  .label--original .variant-name { left: 86px; top: 362px; }
  .label--lemon .variant-name { left: 0; right: 0; text-align: center; top: 392px; }
</style>
</head>
<body>
  <main class="canvas">
    <section class="label label--original" aria-label="Original washing up liquid label">
      <div class="brand"><span class="brand-dot"></span>Marlow Brite</div>
      <div class="artwork" role="img" aria-label="Illustration of soap bubbles"></div>
      <div class="variant-name">ORIGINAL</div>
    </section>
    <section class="label label--lemon" aria-label="Lemon washing up liquid label">
      <div class="brand"><span class="brand-dot"></span>Marlow Brite</div>
      <div class="artwork" role="img" aria-label="Illustration of a lemon slice with soap bubbles"></div>
      <div class="variant-name">LEMON</div>
    </section>
  </main>
</body>
</html>
```